Owen Tasker Studios Business Card

Looking for a clear, modern, elegant, sharp business card that conveys a professional yet edgy image to my business as a wedding, portrait, and travel photographer. Would like something that looks vintage yet modern. Need a new business card to grow my business. We are growing the business for Wedding and Event Photography as well as fine art Photography. (Mostly Landscapes)
Updates

I’m looking through designs now but I have a new logo that i want using please.

New logo uploaded please redesign using that

PLEASE ALL DESIGNERS LOOK IN BRIEF FOR NEW LOGO

Target Market(s)

Brides, Grooms, Families with Kids, People looking for Fine Art Photography Artwork

Industry/Entity Type

Photographer

Contact Information for Business Card

Unsure

Font styles to use
Serif

Colors

Designer to choose colors to be used in the design.

Requirements
Must have
• My Website:
• http://taskerlens.examplefolio.net
• Phone:
• 323-481-5206
• Email:
• owentaskerlens@mailbox-example.net
Nice to have
• Would like a sort of shine on the printing finish.
• I like black I think it looks good on a business card.
• Can try working with my logo (png that I've attached)

```html
<!DOCTYPE html>
<html lang="en">
<head>
<meta charset="utf-8">
<title>Owen Tasker Studios Business Card</title>
<link href="https://fonts.googleapis.com/css2?family=Lato:wght@300;400;700&display=swap" rel="stylesheet">
<style>
  :root {
    --backdrop: #4b4b4b;
    --card: #262626;
    --ink-light: #ececec;
    --ink-soft: #c4c4c4;
    --ink-dark: #1e1e1e;
    --paper: #ffffff;
  }
  * { margin: 0; padding: 0; box-sizing: border-box; }
  html, body {
    width: 1200px; height: 1200px; overflow: hidden;
    background: var(--backdrop);
    font-family: 'Lato', sans-serif;
  }
  .card {
    position: absolute; left: 212px; width: 776px;
    background: var(--card);
    color: var(--ink-light);
    box-shadow: 0 6px 18px rgba(0,0,0,0.35);
  }
  .card--front { top: 112px; height: 432px; }
  .card--back { top: 658px; height: 430px; overflow: hidden; }

  .front-frame {
    position: absolute; left: 64px; top: 60px; width: 648px; height: 312px;
    border: 2px solid var(--ink-light);
  }
  .brand-square {
    position: absolute; border: 2px solid var(--ink-light);
  }
  .card--front .brand-square { left: 342px; top: 110px; width: 93px; height: 93px; }
  .card--back .brand-square { left: 353px; top: 22px; width: 70px; height: 70px; }

  .brand-name {
    position: absolute; left: 0; width: 100%; text-align: center;
    font-weight: 300; color: var(--ink-light); line-height: 1;
  }
  .brand-name .line { display: block; }
  .card--front .brand-name { top: 232px; }
  .card--front .brand-name .primary { font-size: 43px; }
  .card--front .brand-name .secondary { font-size: 18px; letter-spacing: 0.62em; margin-top: 18px; padding-left: 0.62em; }
  .card--back .brand-name { top: 114px; }
  .card--back .brand-name .primary { font-size: 33px; }
  .card--back .brand-name .secondary { font-size: 14px; letter-spacing: 0.62em; margin-top: 12px; padding-left: 0.62em; }

  .url-tag {
    position: absolute; left: 255px; top: 356px; width: 267px; height: 29px;
    background: var(--paper); color: var(--ink-dark);
    font-size: 13px; font-weight: 700;
    display: flex; align-items: center; justify-content: center;
  }

  .person {
    position: absolute; left: 0; width: 100%; top: 196px; text-align: center;
    color: var(--ink-soft); line-height: 1;
  }
  .person .name { font-size: 26px; font-weight: 400; }
  .person .name strong { font-weight: 700; }
  .person .role { font-size: 18px; color: var(--ink-light); margin-top: 4px; }

  .divider {
    position: absolute; left: 62px; top: 277px; width: 652px; height: 1.5px;
    background: var(--ink-light);
  }
  .contacts { position: absolute; left: 276px; top: 288px; list-style: none; }
  .contact {
    display: flex; align-items: center; height: 41px;
    font-size: 14px; color: var(--ink-light);
  }
  .contact svg { width: 36px; height: 36px; margin-right: 10px; flex: none; }
  .bottom-band {
    position: absolute; left: 0; bottom: 0; width: 100%; height: 17px;
    background: var(--paper);
  }
</style>
</head>
<body>
  <section class="card card--front">
    <div class="front-frame"></div>
    <div class="brand-square"></div>
    <h1 class="brand-name"><span class="line primary">OWEN TASKER</span><span class="line secondary">STUDIOS</span></h1>
    <div class="url-tag">http://taskerlens.examplefolio.net</div>
  </section>

  <section class="card card--back">
    <div class="brand-square"></div>
    <h2 class="brand-name"><span class="line primary">OWEN TASKER</span><span class="line secondary">STUDIOS</span></h2>
    <div class="person">
      <div class="name"><strong>Owen</strong> Tasker</div>
      <div class="role">Founder</div>
    </div>
    <div class="divider"></div>
    <ul class="contacts">
      <li class="contact">
        <svg viewBox="0 0 36 36" aria-hidden="true"><circle cx="18" cy="18" r="16" fill="none" stroke="#ececec" stroke-width="2"/><path d="M13 10c1-1 2-1 3 0l2 3c.5 1 0 2-1 2.5-.5.3-.5 1 0 2l2 3c.5.8 1.2 1 2 .6 1-.6 2-.4 2.6.5l1.6 2.6c.5 1 0 2-1 2.6-3 1.5-6-1-8.5-5S9.5 13 13 10z" fill="#ececec"/></svg>
        323-481-5206
      </li>
      <li class="contact">
        <svg viewBox="0 0 36 36" aria-hidden="true"><circle cx="18" cy="18" r="16" fill="none" stroke="#ececec" stroke-width="2"/><rect x="9.5" y="12" width="17" height="12" fill="none" stroke="#ececec" stroke-width="1.8"/><path d="M9.5 12l8.5 7 8.5-7M9.5 24l6-5.5M26.5 24l-6-5.5" fill="none" stroke="#ececec" stroke-width="1.6"/></svg>
        owentaskerlens@mailbox-example.net
      </li>
      <li class="contact">
        <svg viewBox="0 0 36 36" aria-hidden="true"><circle cx="18" cy="18" r="16" fill="none" stroke="#ececec" stroke-width="2"/><g fill="none" stroke="#ececec" stroke-width="1.4"><circle cx="18" cy="18" r="9"/><ellipse cx="18" cy="18" rx="4" ry="9"/><path d="M9 18h18M10.5 13.5h15M10.5 22.5h15"/></g></svg>
        http://taskerlens.examplefolio.net
      </li>
    </ul>
    <div class="bottom-band"></div>
  </section>
</body>
</html>
```